Business Card Design

I require the design of business cards using my exisiting logo.

It is essential that the designer has experience with various print processes (foil stamping etc) and different paper stock.

The design is to blend in with current packaging and display unit. (Images will be provided).
A swing tag and certificate of authenticity design will als be required at a later stage.

Details which need to be included on the card are:
- Contact Name
- Position in Company
- Address
- Contact Number
- Email Address
- Web Address

Ideally I would prefer the background (both sides) to be greyish colour (offset printing or if you can suggest greyish paperstock) with silver foiling on the front and either black or metallic silver on the back.

Or another option would be grey background on the front and either white or black on the the back.

* The business card can be portrait or landscape.

Printers specifications:
Bleed 3mm
Trim Marks
Seperate file for foil printing

This task is for someone who is creative and enjoys working with fashion and luxury items!
_______________________________________________

I will require business cards designs for 2 different business and would hope to work with the same designer.

Please note I had asked for a grey colour at least on one of the sides. However I keep on getting black and white designs.   

Business

• - Double sided business card
- Luxury feel
- Foil Print Priniting

- Would prefer at least grey background at least on one side of the card.

- The business card can be portrait or landscape.
• *The business card can be portrait or landscape.
• - Bright Colours
- Alterations to logo

```html
<!DOCTYPE html>
<html lang="en">
<head>
<meta charset="utf-8">
<title>Orla Gems — Business Card</title>
<link rel="stylesheet" href="https://fonts.googleapis.com/css2?family=Oswald:wght@200;300&display=swap">
<style>
  :root {
    --page: #e4e1dc;
    --card: #3a3a3d;
    --foil: #d2d3d7;
    --foil-soft: #a9aaaf;
    --shadow: rgba(0, 0, 0, 0.28);
  }
  * { margin: 0; padding: 0; box-sizing: border-box; }
  html, body {
    width: 1200px;
    height: 880px;
    overflow: hidden;
    background: var(--page);
  }
  .sheet {
    width: 1200px;
    height: 880px;
    display: flex;
    flex-direction: column;
    align-items: center;
    justify-content: center;
    gap: 50px;
  }
  .card {
    position: relative;
    width: 630px;
    height: 360px;
    background: var(--card);
    overflow: hidden;
    box-shadow: 0 10px 26px var(--shadow);
    font-family: "Oswald", sans-serif;
    font-weight: 200;
    color: var(--foil);
  }

  .brand-name {
    font-family: "Oswald", sans-serif;
    font-weight: 200;
    color: var(--foil);
    letter-spacing: 0.02em;
    white-space: nowrap;
  }

  /* Front */
  .card-front .brand-mark {
    position: absolute;
    left: 88px;
    top: 78px;
    width: 92px;
    height: 92px;
    border: 2px solid var(--foil);
    border-radius: 50%;
  }
  .card-front .brand-name {
    position: absolute;
    left: 36px;
    top: 196px;
    width: 196px;
    text-align: center;
    font-size: 44px;
  }
  .card-front .divider {
    position: absolute;
    left: 272px;
    top: 58px;
    width: 1px;
    height: 244px;
    background: var(--foil);
  }
  .contact {
    position: absolute;
    left: 302px;
    top: 70px;
    line-height: 1.2;
  }
  .contact-name {
    font-size: 26px;
    letter-spacing: 0.03em;
    text-transform: uppercase;
  }
  .contact-role {
    font-size: 15px;
    color: var(--foil-soft);
    margin-bottom: 28px;
  }
  .contact-lines {
    list-style: none;
    font-size: 19px;
    line-height: 1.28;
  }

  /* Back */
  .card-back .brand-name {
    position: absolute;
    left: 40px;
    top: 150px;
    font-size: 50px;
  }
  .card-back .motif {
    position: absolute;
    left: 300px;
    top: 0;
  }
</style>
</head>
<body>
<main class="sheet">
  <section class="card card-front" aria-label="Business card front">
    <span class="brand-mark" aria-hidden="true"></span>
    <p class="brand-name">ORLA GEMS</p>
    <span class="divider" aria-hidden="true"></span>
    <div class="contact">
      <p class="contact-name">Martin Vale</p>
      <p class="contact-role">manager</p>
      <ul class="contact-lines">
        <li>Your Address Goes Here</li>
        <li>0555-20-4816</li>
        <li>office@orla-gems.com</li>
        <li>www.orla-gems.com</li>
      </ul>
    </div>
  </section>

  <section class="card card-back" aria-label="Business card back">
    <p class="brand-name">ORLA GEMS</p>
    <svg class="motif" width="330" height="360" viewBox="0 0 330 360" aria-hidden="true">
      <circle cx="210" cy="190" r="170" fill="none" stroke="#d2d3d7" stroke-width="3"/>
    </svg>
  </section>
</main>
</body>
</html>
```